'Cradle Ahead' promotional brochure

We have designed a 6 week program to educate impending first-time parents about the things they need to know to survive the first 6 months. Sessions delivered by general practitioner/family doctor, dietician, physiotherapist, speech pathologist and psychologist. Our promotional blurb is: 'A comprehensive education program for first-time parents-to-be, delivered over 6 weeks by health professionals in your community, about everything you need to know to look after your baby (and yourself!) in the first 6 months'. I now want to put together a promotional brochure to be distributed to those couples who express an interest which will provide further details of what will be delivered in the course.
Updates
In terms of layout, I envisaged a double sided A4 size, foldable into 3 sections, but very happy to be guided on this.
Target Market(s)
To appeal to a young, well educated demographic. First time parents couples.
Industry/Entity Type
Medical
Font styles to use
Other font styles liked:
- Playfair Display
Requirements
Must have
- Playfair display font to be consistent with our logo (attached). Logo also included please. Some consistency with colours of logo please.
Nice to have
- I am a doctor, and have no creative genes! But prefer a clean and professional appearance overall. Not too cluttered in overall appearance.
Should not have
- No cheesy pictures of babies.

```html
<!DOCTYPE html>
<html lang="en">
<head>
<meta charset="utf-8">
<title>Cradle Ahead – Program Brochure</title>
<link href="https://fonts.googleapis.com/css2?family=Playfair+Display:wght@400;700;900&family=Open+Sans:wght@400;600&display=swap" rel="stylesheet">
<style>
:root{
  --green:#8cc63f;
  --ink:#111111;
  --paper:#ffffff;
  --backdrop:#e4e4e6;
  --grey:#7a7a7a;
}
*{box-sizing:border-box;margin:0;padding:0}
html,body{width:1200px;height:857px;overflow:hidden;background:var(--backdrop)}
body{position:relative;font-family:"Open Sans",Arial,sans-serif;color:var(--ink)}
.page{position:absolute;top:44px;width:545px;height:770px;background:var(--paper);overflow:hidden;box-shadow:0 4px 14px rgba(0,0,0,.18)}
.page--front{left:40px}
.page--inside{left:615px}
.band{position:absolute;left:0;top:0;width:545px;height:770px}
.hero-photo{position:absolute;left:0;top:0;width:545px;height:470px;
  background:radial-gradient(ellipse at 55% 45%,#f3d9cc 0%,#f6e6de 35%,#fbf5f2 65%,#ffffff 90%)}
.brand{position:absolute;right:-30px;top:-150px;width:310px;height:310px;border-radius:50%;background:var(--paper);border:4px solid var(--green)}
.brand__inner{position:absolute;left:60px;top:185px;display:flex;align-items:center;gap:12px}
.brand__dot{width:34px;height:34px;border-radius:50%;background:var(--green)}
.brand__name{font-family:"Playfair Display",Georgia,serif;font-size:17px;line-height:1.05;color:var(--grey);letter-spacing:.5px}
.title{position:absolute;left:100px;top:220px;font-family:"Playfair Display",Georgia,serif;font-weight:900;font-size:72px;line-height:.95;color:var(--ink);text-shadow:4px 3px 0 var(--green);text-transform:uppercase}
.title span{display:block}
.title span+span{padding-left:50px}
.week{position:absolute;left:22px}
.week__tag{display:inline-block;background:var(--ink);color:#fff;font-family:"Playfair Display",Georgia,serif;font-weight:700;font-size:18px;line-height:24px;padding:0 16px 0 10px}
.week__lead{font-size:10px;line-height:14px;margin-top:3px}
.week__sub{font-family:"Playfair Display",Georgia,serif;font-size:14px;line-height:18px;margin-top:2px}
.week__list{list-style:none;font-size:10px;line-height:14px;margin-top:2px}
.week__list li::before{content:"";display:inline-block;width:4px;height:4px;border-radius:50%;background:var(--ink);margin:0 6px 2px 4px}
.session{display:block;width:230px;background:var(--green);font-family:"Playfair Display",Georgia,serif;font-size:13px;line-height:18px;padding:0 10px;margin-top:4px}
.session--plain{background:none;padding:0}
.session--light{color:#fff}
.week__text{font-size:10px;line-height:14px;margin-top:2px}
.week--w1{top:440px;width:470px}
.week--w2{top:598px;width:500px}
.week--w3{top:58px;width:500px}
.week--w4{top:252px;width:300px}
.week--w5{top:432px;width:480px}
.week--w6{top:540px;width:500px}
.round-photo{position:absolute;left:345px;top:250px;width:180px;height:180px;border-radius:50%;border:4px solid var(--green);
  background:radial-gradient(circle at 45% 40%,#f1d2bd 0%,#e9c4ab 35%,#f4ece6 70%,#ffffff 100%)}
</style>
</head>
<body>

<section class="page page--front">
  <div class="hero-photo" role="img" aria-label="Soft photo of a parent's hand holding a newborn's tiny hand"></div>
  <svg class="band" viewBox="0 0 545 770" aria-hidden="true">
    <polygon points="0,450 545,320 545,430 0,595" fill="#8cc63f"/>
  </svg>
  <div class="brand">
    <div class="brand__inner">
      <span class="brand__dot"></span>
      <span class="brand__name">WATTLEBROOK<br>HEALTH &amp;<br>MEDICAL</span>
    </div>
  </div>
  <h1 class="title"><span>Cradle</span><span>Ahead</span></h1>

  <div class="week week--w1">
    <span class="week__tag">Week 1</span>
    <p class="week__lead">GP Dr Maren Holloway will share information for Mum's own health after delivery.</p>
    <p class="week__sub">Topics include:</p>
    <ul class="week__list">
      <li>Vaccinations in pregnancy</li>
      <li>Bleeding, bladder and bowel after delivery</li>
      <li>Breastfeeding, engorgement and mastitis</li>
      <li>Bottle feeding</li>
      <li>Post-natal anxiety &amp; depression</li>
      <li>Intimacy and contraception</li>
    </ul>
  </div>

  <div class="week week--w2">
    <span class="week__tag">Week 2</span>
    <span class="session">Session 1</span>
    <p class="week__text">Clinical Psychologist Dr Tessa Quinlan will discuss changes in relationships as couples becomes parents, gender roles in parenting and post-natal depression.</p>
    <span class="session">Session 2</span>
    <p class="week__text">Physiotherapist Lara Whitfield will present advice for Mums regarding exercise during and after pregnancy, looking after the pelvic floor during and after pregnancy, and abdominal muscle separation management. She will also provide advice for promoting babies' neck strength and minimising the risk of flat spots on the head and encouraging gross motor skills in the first 6 months.</p>
  </div>
</section>

<section class="page page--inside">
  <svg class="band" viewBox="0 0 545 770" aria-hidden="true">
    <polygon points="0,60 545,20 545,200 0,245" fill="#8cc63f"/>
    <polygon points="0,520 545,420 545,770 0,770" fill="#8cc63f"/>
  </svg>

  <div class="week week--w3">
    <span class="week__tag">Week 3</span>
    <span class="session session--plain session--light">Session 1</span>
    <p class="week__text">Dietician Nadia Brennan provides advice for Mums regarding healthy eating during pregnancy and lactation, normal weight gain during pregnancy and realistic weight loss after. She will also discuss the evidence regarding breastfeeding VS bottle-feeding, normal infant weight gain and introducing solids (including those with potential for allergy).</p>
    <span class="session session--plain session--light">Session 2</span>
    <p class="week__text">Paediatric Speech Pathologist Ruth Ashdown will share information about latching and breast-feeding troubles &amp; tongue tie, advice about dummies and finger-sucking, introducing solids &amp; feeding (including 'pouch' food), encouraging language development and current evidence about electronic devices impacting language development.</p>
  </div>

  <div class="round-photo" role="img" aria-label="Photo of a smiling baby lying on a soft white blanket"></div>

  <div class="week week--w4">
    <span class="week__tag">Week 4</span>
    <p class="week__lead">GP Dr Maren Holloway will share advice about your babies' health in the first 6 months, including:</p>
    <ul class="week__list">
      <li>Skin of newborns</li>
      <li>Sleeping</li>
      <li>Crying</li>
      <li>Immunisations</li>
      <li>Fever and infections</li>
      <li>Diarrhoea and constipation</li>
      <li>Teething</li>
      <li>Understanding a baby's signals</li>
    </ul>
  </div>

  <div class="week week--w5">
    <span class="week__tag">Week 5</span>
    <span class="session">Session 1</span>
    <p class="week__text">Clinical Psychologist Dr Tessa Quinlan will share information about bonding &amp; attachment with your baby, how to promote their social &amp; emotional development and how to manage separation anxiety. She will also discuss positive parenting approaches.</p>
  </div>

  <div class="week week--w6">
    <span class="week__tag">Week 6</span>
    <span class="session session--plain">Session 1</span>
    <p class="week__text">Secret Men's Business – a men-only session (including beer!) with a new father for frank discussion about the road ahead. Mums will do a shopping excursion with the GP &amp; Dietician to Greenway to look at baby products and food – the good and the bad!</p>
    <span class="session session--plain">Session 2</span>
    <p class="week__text">Program review, reflection and evaluation and future session planning when baby is 6 months of age.</p>
  </div>
</section>

</body>
</html>
```